Create a Graphic About YOURSELF and PixelHarbor

PixelHarbor would like you (designers) to create an awesome graphic to promote YOURSELF and your profile on PixelHarbor!

Your graphic should communicate your name, your services and should mention PixelHarbor.

The design should be perfect for sharing on Chatterly. Here's an example of what we'd like http://blog.pixelharbor-example.ca/article/333/pixelharbor-launches-3000-hire-me-social-design-contest

Once you submitted your design, we'd love you to share the design ('advertisement') and promote yourself and PixelHarbor to your friends and potential customers. So make your submissions great and get your friends to vote for your design by 'Liking' it on Chatterly!

Prizes:
$1500 - "PixelHarbor Community" prize awarded to the designer with the most Chatterly 'Likes'
5 x $50 for the next 5 'most liked' designs on Chatterly

$1000 - "Hire Me" prize awarded to the designer who receives the most client invites
5 x $50 for the next 5 'most invited' designers

In summary, this is a great opportunity for you to increase your exposure to PixelHarbor customers and win cash prizes. Show off your design skills and get hired by PixelHarbor customers from around the world!

Target Market(s)

Fans, friends and customers of YOU

Industry/Entity Type

Cash

Requirements
Must have
• 1) Include your PixelHarbor user name on the graphic so customers can find you in the PixelHarbor Designer Directory
2) Include the tagline "Hire Me on PixelHarbor.com!" in your graphic design.
3) Share your design's URL on our Chatterly wall at http://chatterly-example.com/pixelharbor and get your friends to 'like' your design.
Nice to have
• 1) Include a tagline that expresses your design approach/philosophy
2) Artwork dimensions: 403 x 403 px
3) You can submit more than 1 design!
Should not have
• You must own the copyright of any images you use including stock imagery.

```html
<!DOCTYPE html>
<html lang="en">
<head>
<meta charset="utf-8">
<title>Kiran Verma – Hire Me on PixelHarbor.com</title>
<link rel="stylesheet" href="https://fonts.googleapis.com/css2?family=Ribeye&family=Archivo+Black&family=Arimo:wght@700&display=swap">
<style>
  :root {
    --page: #ffffff;
    --board: #1f1b1a;
    --board-edge: #8cc63f;
    --name-green: #a9d035;
    --white: #ffffff;
    --stationery-grey: #a7a5a3;
    --icon-red: #e8605a;
    --banner-blue: #8fb4e8;
    --bus-yellow: #f6c932;
    --bus-shade: #e9a521;
    --bus-band: #2a2420;
    --school-red: #c8493a;
    --school-cream: #f1dfae;
    --tree-green: #6bb33a;
  }
  html, body {
    margin: 0;
    padding: 0;
    width: 1200px;
    height: 1200px;
    overflow: hidden;
    background: var(--page);
  }
  .promo-canvas {
    display: block;
    width: 1200px;
    height: 1200px;
  }
  .board { fill: var(--board); stroke: var(--board-edge); stroke-width: 18; }
  .designer-name {
    font-family: "Ribeye", "Archivo Black", fantasy;
    font-size: 80px;
    fill: var(--name-green);
    letter-spacing: 2px;
  }
  .name-rule { stroke: var(--name-green); stroke-width: 5; stroke-linecap: round; }
  .service { font-family: "Arimo", "Archivo Black", sans-serif; font-weight: 700; }
  .service-logo { font-size: 62px; fill: var(--white); }
  .service-stationery { font-size: 38px; fill: var(--stationery-grey); }
  .service-icon { font-family: "Archivo Black", sans-serif; font-size: 58px; fill: var(--icon-red); }
  .service-banner { font-family: "Archivo Black", sans-serif; font-size: 38px; fill: var(--banner-blue); }
  .hire-band { fill: var(--bus-band); }
  .hire-tagline {
    font-family: "Archivo Black", sans-serif;
    font-size: 36px;
    fill: var(--white);
  }
</style>
</head>
<body>
<svg class="promo-canvas" viewBox="0 0 1200 1200" xmlns="http://www.w3.org/2000/svg">
  <defs>
    <linearGradient id="schoolTones" x1="0" y1="0" x2="1" y2="1">
      <stop offset="0" stop-color="var(--school-red)"/>
      <stop offset="0.55" stop-color="var(--school-cream)"/>
      <stop offset="1" stop-color="var(--tree-green)"/>
    </linearGradient>
    <linearGradient id="treeTones" x1="0" y1="0" x2="0" y2="1">
      <stop offset="0" stop-color="var(--tree-green)"/>
      <stop offset="1" stop-color="#8a5a2b"/>
    </linearGradient>
    <linearGradient id="busTones" x1="0" y1="0" x2="0" y2="1">
      <stop offset="0" stop-color="var(--bus-yellow)"/>
      <stop offset="1" stop-color="var(--bus-shade)"/>
    </linearGradient>
  </defs>

  <!-- chalkboard panel -->
  <rect class="board" x="24" y="92" width="1078" height="810" rx="120" ry="120"/>

  <!-- scenery -->
  <rect class="school-scene" role="img" aria-label="Illustration of a small school building with trees and flowers"
        x="208" y="0" width="432" height="134" rx="24" fill="url(#schoolTones)"/>
  <rect class="side-tree" role="img" aria-label="Illustration of a small green tree"
        x="1087" y="238" width="105" height="119" rx="40" fill="url(#treeTones)"/>

  <!-- school bus -->
  <rect class="school-bus" role="img" aria-label="Illustration of a yellow school bus carrying happy children"
        x="447" y="805" width="745" height="371" rx="60" fill="url(#busTones)"/>
  <rect class="hire-band" x="495" y="1016" width="680" height="68" rx="10"/>
  <text class="hire-tagline" x="835" y="1063" text-anchor="middle" textLength="640" lengthAdjust="spacingAndGlyphs">HIRE ME ON PIXELHARBOR.COM</text>

  <!-- designer name -->
  <g transform="rotate(-8.5 542 351)">
    <text class="designer-name" x="542" y="380" text-anchor="middle" textLength="880" lengthAdjust="spacingAndGlyphs">KIRAN VERMA</text>
  </g>
  <line class="name-rule" x1="90" y1="462" x2="983" y2="352"/>

  <!-- services -->
  <g transform="rotate(-7 604 560)">
    <text class="service service-logo" x="600" y="564" text-anchor="middle" textLength="470" lengthAdjust="spacingAndGlyphs">LOGO Design</text>
    <text class="service service-stationery" x="450" y="638" text-anchor="middle" textLength="330" lengthAdjust="spacingAndGlyphs">STATIONERY</text>
    <text class="service service-icon" x="520" y="704" text-anchor="middle" textLength="440" lengthAdjust="spacingAndGlyphs">ICON DESIGN</text>
    <text class="service service-banner" x="640" y="754" text-anchor="middle" textLength="500" lengthAdjust="spacingAndGlyphs">BANNER AD DESIGN</text>
  </g>
</svg>
</body>
</html>
```